Law practice business card

I have an existing logo that I would like to make a little cleaner and maybe something more creative, but using the same base. I would like a contempoary design of the business card.

Industry/Entity Type

Law

Logo Text

On one side of the card - below the logo - I would want to say "BRANTOVE" and below that it should read "LAW OFFICES, PC" in smaller print. If you have somethign more creative, I would love to see it.

Logo styles of interest
Lettermark Logo
Font styles to use
Sans Serif

Colors

Designer to choose only greyscale colors for use in the design.

Requirements
Must have
• Standard info: My name with "Attorney at Law" underneath; phone, fax, address, email and website.

```html
<!DOCTYPE html>
<html lang="en">
<head>
<meta charset="utf-8">
<title>Brantove Law Offices – Business Card</title>
<link rel="stylesheet" href="https://fonts.googleapis.com/css2?family=Montserrat:wght@400;600;700&display=swap">
<style>
  :root {
    --page: #262626;
    --card: #0b0b0b;
    --accent: #b8b8b8;
    --accent-soft: #5e5e5e;
    --text-light: #e6e6e6;
  }
  * { box-sizing: border-box; margin: 0; padding: 0; }
  html, body { width: 1200px; height: 900px; overflow: hidden; }
  body {
    background: var(--page);
    display: flex;
    flex-direction: column;
    align-items: center;
    justify-content: center;
    gap: 48px;
    font-family: "Montserrat", sans-serif;
  }
  .card {
    position: relative;
    width: 640px;
    height: 366px;
    border-radius: 34px;
    background: var(--card);
    overflow: hidden;
    box-shadow: 0 14px 36px rgba(0,0,0,.55);
  }

  /* front */
  .card-front .pattern-field {
    position: absolute; inset: 0;
    background: linear-gradient(135deg, #1b1b1b 0%, #0b0b0b 45%, #161616 100%);
  }
  .card-front .brand-mark {
    position: absolute;
    right: 92px; top: 150px;
    display: flex; align-items: center; gap: 10px;
  }
  .brand-square {
    width: 14px; height: 14px;
    background: var(--accent);
  }
  .brand-name-small {
    font-weight: 700;
    font-size: 20px;
    letter-spacing: 2px;
    color: var(--accent);
  }

  /* back */
  .firm-block {
    position: absolute;
    right: 46px; top: 86px;
    text-align: right;
  }
  .firm-name {
    font-weight: 700;
    font-size: 42px;
    letter-spacing: 2px;
    line-height: 1;
    color: var(--accent);
  }
  .firm-tagline {
    margin-top: 10px;
    font-weight: 400;
    font-size: 13px;
    letter-spacing: 6px;
    color: var(--accent);
  }
  .divider {
    position: absolute;
    left: 214px; right: 0; top: 198px;
    height: 1px;
    background: var(--accent-soft);
  }
  .attorney {
    position: absolute;
    left: 44px; top: 186px;
  }
  .attorney-name {
    font-weight: 700;
    font-size: 22px;
    letter-spacing: 1px;
    line-height: 1;
    color: var(--accent);
  }
  .attorney-title {
    margin-top: 6px;
    font-weight: 400;
    font-size: 15px;
    color: var(--text-light);
  }
  .contact-list {
    position: absolute;
    left: 60px; top: 258px;
    list-style: none;
    font-weight: 400;
    font-size: 14px;
    color: var(--text-light);
  }
  .contact-list li {
    display: flex; align-items: center; gap: 8px;
    height: 26px;
  }
  .contact-list .sep { color: var(--accent-soft); margin: 0 4px; }
  .icon { width: 13px; height: 13px; fill: var(--accent); flex: none; }
</style>
</head>
<body>

<section class="card card-front" aria-label="Card front">
  <div class="pattern-field" role="img" aria-label="Repeating dark diamond pattern in black and grey"></div>
  <div class="brand-mark">
    <span class="brand-square"></span>
    <span class="brand-name-small">BRANTOVE</span>
  </div>
</section>

<section class="card card-back" aria-label="Card back">
  <div class="firm-block">
    <div class="firm-name">BRANTOVE</div>
    <div class="firm-tagline">LAW OFFICES, PC</div>
  </div>

  <div class="divider"></div>

  <div class="attorney">
    <div class="attorney-name">BRANTOVE</div>
    <div class="attorney-title">Attorney at Law</div>
  </div>

  <ul class="contact-list">
    <li>
      <svg class="icon" viewBox="0 0 16 16"><path d="M8 0a5.5 5.5 0 0 0-5.5 5.5C2.5 10 8 16 8 16s5.5-6 5.5-10.5A5.5 5.5 0 0 0 8 0zm0 8a2.5 2.5 0 1 1 0-5 2.5 2.5 0 0 1 0 5z"/></svg>
      11 dummy city, 00 dummy place
    </li>
    <li>
      <svg class="icon" viewBox="0 0 16 16"><path d="M3.6 1 6 3.7 4.6 5.6a9 9 0 0 0 5.8 5.8L12.3 10l2.7 2.4-1.6 2.4C7.4 15 1 8.6 1.2 2.6z"/></svg>
      (00) 0000 0000
      <span class="sep">|</span>
      <svg class="icon" viewBox="0 0 16 16"><path d="M4 1h6v4H4zM2 6h12v7H2zm2 2v1h2V8zm4 0v1h2V8zM4 10v1h2v-1zm4 0v1h2v-1z"/></svg>
      (00) 0000 0000
    </li>
    <li>
      <svg class="icon" viewBox="0 0 16 16"><path d="M1 3h14v10H1zm1.5 1.5L8 9l5.5-4.5z"/></svg>
      info@brantove.com
      <span class="sep">|</span>
      <svg class="icon" viewBox="0 0 16 16"><path d="M8 0a8 8 0 1 0 0 16A8 8 0 0 0 8 0zm0 1.5c.9 1.3 1.5 3 1.7 5.7H6.3C6.5 4.5 7.1 2.8 8 1.5zM1.6 8.8h3.1c.1 2.3.6 4 1.4 5.3a6.5 6.5 0 0 1-4.5-5.3zm0-1.6a6.5 6.5 0 0 1 4.5-5.3c-.8 1.3-1.3 3-1.4 5.3zm4.7 1.6h3.4c-.2 2.6-.8 4.3-1.700 5.7-.9-1.4-1.5-3.1-1.7-5.7zm5 0h3.1a6.5 6.5 0 0 1-4.5 5.3c.8-1.3 1.3-3 1.4-5.3zm0-1.6c-.1-2.3-.6-4-1.4-5.3a6.5 6.5 0 0 1 4.5 5.3z"/></svg>
      www.brantove.com
    </li>
  </ul>
</section>

</body>
</html>
```